Business Card Design Project for - The Pellowick Greenworks Company Ltd. We are a Landscape and garden

I would like designer to use all special glosses etc so i can have a professional looking business card. The theme of the business card can reflect that of the Logo attached by MarkQuarry or your own unique ideas.. please feel free to go wild as i hope i can select a winner i like - my budget will be committed so please get involved. Good luck and thank you Lyndon

Target Market(s)

Must look Professional

General Public and Businesses including Councils, Local Government, Hospitals, Hotels, Professionals and Professional Sports People.

Industry/Entity Type

Landscape Gardening

Contact Information for Business Card

The Pellowick Greenworks Company Ltd

Mr L.R Ashcombe
Head Office - Quayfront Park Manchester
t. 0772 408 916
e. info@pellowickgreenworks.co.uk
w. www.pellowickgreenworks.co.uk

Friendpage - https://www.friendpage-example.com/ThePellowickGreenworksCompany/
Chirpline - https://chirpline-example.com/ThePruningCart
Snapgrid - https://www.snapgrid-example.com/thepellowickgreenworkscompany/?hl=en
Circles - https://circles.searchhub-example.com/u/0/208473950162438571093
Yelp - https://www.reviewnook-example.co.uk/biz/the-pellowick-greenworks-company-manchester-4

Font styles to use
Serif
Script
Other font styles liked:
• I don't have much of an idea of font types sorry

Colors

Designer to choose colors to be used in the design.

Requirements
Must have
• A Professional look and Design
• Special effects with gloss and fading of colours possibly..
• Front and back design
Nice to have
• All special features with effects and gloss etc

```html
<!DOCTYPE html>
<html lang="en">
<head>
<meta charset="utf-8">
<title>The Pellowick Greenworks Company Ltd – Business Card</title>
<link href="https://fonts.googleapis.com/css2?family=Cinzel:wght@400;500&family=Arvo:wght@400;700&display=swap" rel="stylesheet">
<style>
  :root{
    --page:#ffffff;
    --card:#222427;
    --card-panel:#17191b;
    --silver:#aeb4b8;
    --ink:#f2f2f2;
    --rule:#4a4e52;
    --icon:#121314;
    --leaf:#5fd62a;
    --glow:#8d9194;
  }
  *{margin:0;padding:0;box-sizing:border-box}
  html,body{width:1200px;height:1200px;overflow:hidden;background:var(--page)}
  .canvas{position:relative;width:1200px;height:1200px}
  .card{position:absolute;left:339px;width:508px;height:290px;background:var(--card);overflow:hidden}
  .card--front{top:135px}
  .card--back{top:645px}
  .corner-glow{position:absolute;right:0;bottom:0;width:130px;height:130px;
    background:radial-gradient(circle at 85% 75%,rgba(141,145,148,.85) 0%,rgba(141,145,148,.45) 40%,rgba(141,145,148,0) 72%)}

  /* front */
  .front-mark{position:absolute;left:218px;top:48px;width:70px;height:70px;border-radius:50%;
    background:radial-gradient(circle at 35% 30%,#b8f58a 0%,var(--leaf) 45%,#2c8a10 100%)}
  .front-name{position:absolute;left:0;width:100%;text-align:center;font-family:"Cinzel",serif;font-weight:500;color:var(--silver)}
  .front-name--main{top:150px;font-size:33px;letter-spacing:2px}
  .front-name--sub{top:206px;font-size:12.5px;letter-spacing:3.2px}

  /* back */
  .person{position:absolute;left:44px;top:40px;font-family:"Arvo",serif;font-size:21px;color:var(--ink)}
  .person-rule{position:absolute;left:46px;top:75px;width:210px;height:1px;background:var(--rule)}
  .contact{position:absolute;left:27px;display:flex;align-items:center;gap:12px;font-family:"Arvo",serif;font-weight:700;font-size:12px;color:var(--ink)}
  .contact svg{width:26px;height:22px;flex:none}
  .contact--phone{top:92px}
  .contact--mail{top:123px}
  .contact--web{top:151px}
  .logo-panel{position:absolute;left:290px;top:0;width:200px;height:158px;background:var(--card-panel);
    border-radius:0 0 4px 4px;box-shadow:0 3px 8px rgba(0,0,0,.55)}
  .panel-mark{position:absolute;left:81px;top:64px;width:38px;height:38px;border-radius:50%;
    background:radial-gradient(circle at 35% 30%,#b8f58a 0%,var(--leaf) 45%,#2c8a10 100%)}
  .panel-name{position:absolute;left:0;width:100%;text-align:center;font-family:"Cinzel",serif;font-weight:500;color:var(--silver)}
  .panel-name--main{top:117px;font-size:15.5px;letter-spacing:1px}
  .panel-name--sub{top:141px;font-size:6.5px;letter-spacing:1.3px}
  .socials{position:absolute;left:20px;top:198px;display:flex;height:84px}
  .social{display:flex;flex-direction:column;align-items:center;
    font-family:"Arvo",serif;font-weight:700;font-size:8.5px;line-height:11px;color:var(--silver);text-align:center;padding:4px 3px 0}
  .social + .social{border-left:1px solid var(--icon)}
  .social-network{font-family:"Arvo",serif;font-weight:700;font-size:9px;color:var(--icon);margin-bottom:9px}
  .social--a{width:80px}
  .social--b{width:103px}
  .social--c{width:105px}
  .social--d{width:112px}
</style>
</head>
<body>
<div class="canvas">

  <section class="card card--front">
    <div class="corner-glow" role="img" aria-label="Soft grey light-glow decoration"></div>
    <div class="front-mark"></div>
    <div class="front-name front-name--main">THE PELLOWICK</div>
    <div class="front-name front-name--sub">GREENWORKS COMPANY LTD</div>
  </section>

  <section class="card card--back">
    <div class="corner-glow" role="img" aria-label="Soft grey light-glow decoration"></div>

    <div class="person">Mr L.R Ashcombe</div>
    <div class="person-rule"></div>

    <div class="contact contact--phone">
      <svg viewBox="0 0 26 22" aria-hidden="true"><path d="M5 3c2-1 3 0 4 2l1 2c0 1-1 2-2 3 1 2 3 4 5 5 1-1 2-2 3-2l2 1c2 1 3 2 2 4-1 2-3 3-5 2C10 18 5 13 3 8 2 6 3 4 5 3z" fill="var(--icon)"/><path d="M15 3a6 6 0 0 1 5 5M15 6a3 3 0 0 1 3 3" stroke="var(--icon)" stroke-width="1.5" fill="none"/></svg>
      <span>0772 408 916</span>
    </div>
    <div class="contact contact--mail">
      <svg viewBox="0 0 26 22" aria-hidden="true"><rect x="1" y="3" width="24" height="16" fill="none" stroke="var(--icon)" stroke-width="1.6"/><path d="M1 3l12 9 12-9M1 19l9-8M25 19l-9-8" fill="none" stroke="var(--icon)" stroke-width="1.4"/></svg>
      <span>info@pellowickgreenworks.co.uk</span>
    </div>
    <div class="contact contact--web">
      <svg viewBox="0 0 26 22" aria-hidden="true"><circle cx="13" cy="11" r="10" fill="var(--icon)"/><text x="13" y="14" text-anchor="middle" font-family="Arial, sans-serif" font-size="7" fill="#555">www</text></svg>
      <span>pellowickgreenworks.co.uk</span>
    </div>

    <div class="logo-panel">
      <div class="panel-mark"></div>
      <div class="panel-name panel-name--main">THE PELLOWICK</div>
      <div class="panel-name panel-name--sub">GREENWORKS COMPANY LTD</div>
    </div>

    <div class="socials">
      <div class="social social--a"><span class="social-network">Friendpage</span>ThePellowick<br>Greenworks<br>Company</div>
      <div class="social social--b"><span class="social-network">Chirpline</span>ThePruningCart</div>
      <div class="social social--c"><span class="social-network">Circles</span>https://circles.<br>searchhub-example<br>.com/u/0/2084739<br>50162438571093</div>
      <div class="social social--d"><span class="social-network">Snapgrid</span>thepellowick-<br>greenworkscompany</div>
    </div>
  </section>

</div>
</body>
</html>
```